Criação de Papelaria Profissional para Advocacia e Direito
A empresa queria:
" Ribeiro Tavares Advogados é um escritório boutique de atuação diversificada (full service) "

```html
<!DOCTYPE html>
<html lang="pt-BR">
<head>
<meta charset="utf-8">
<title>Ribeiro Tavares Advogados — Envelopes</title>
<link rel="stylesheet" href="https://fonts.googleapis.com/css2?family=Montserrat:wght@300;400;500&display=swap">
<style>
  :root {
    --backdrop: #ebe8e3;
    --navy: #3f5a72;
    --navy-deep: #24405a;
    --flap-grey: #9c9ea0;
    --flap-light: #e6e6e6;
    --paper: #ffffff;
    --stripe: #b9bcbf;
    --ghost: #dcdcdc;
    --ink: #5a6570;
    --on-navy: #e9eef2;
  }
  * { box-sizing: border-box; margin: 0; padding: 0; }
  html, body { width: 1200px; height: 1200px; overflow: hidden; }
  body {
    background: var(--backdrop);
    font-family: "Montserrat", sans-serif;
    position: relative;
  }
  .envelope {
    position: absolute;
    top: 209px;
    width: 462px;
    height: 746px;
  }
  .envelope--front { left: 118px; }
  .envelope--back { left: 600px; }
  .envelope__flap {
    position: absolute;
    top: 0; left: 0;
    width: 462px; height: 104px;
  }
  .envelope__body {
    position: absolute;
    top: 100px; left: 0;
    width: 462px; height: 646px;
    box-shadow: 0 6px 14px rgba(0,0,0,.18);
  }
  .envelope--front .envelope__body { background: var(--navy); }
  .envelope--back .envelope__body { background: var(--paper); }

  .brand {
    position: absolute;
    top: 180px; left: 0; width: 100%;
    text-align: center;
    color: var(--on-navy);
  }
  .brand__mark {
    width: 24px; height: 24px;
    border: 2px solid var(--on-navy);
    margin: 0 auto 10px;
  }
  .brand__name {
    font-weight: 400;
    font-size: 26px;
    letter-spacing: 2px;
    line-height: 1;
  }
  .brand__tagline {
    font-weight: 300;
    font-size: 8px;
    letter-spacing: 1.5px;
    margin-top: 6px;
    text-transform: uppercase;
    padding-left: 120px;
  }
  .front-stripe {
    position: absolute;
    left: 0; bottom: 62px;
    width: 100%; height: 10px;
    background: var(--stripe);
  }

  .ghost-name {
    position: absolute;
    top: 230px; left: 0; width: 100%;
    text-align: center;
    color: var(--ghost);
    font-weight: 300;
    font-size: 52px;
    letter-spacing: 4px;
    line-height: 1.15;
    text-transform: uppercase;
  }
  .footer-accent {
    position: absolute;
    right: 24px; bottom: 44px;
    width: 92px; height: 6px;
    background: var(--navy-deep);
  }
  .contacts {
    position: absolute;
    left: 24px; right: 24px; bottom: 16px;
    display: flex;
    justify-content: space-between;
    align-items: center;
    font-size: 8px;
    color: var(--ink);
  }
  .contact { display: flex; align-items: center; gap: 5px; }
  .contact svg { width: 11px; height: 11px; }
  .contact__dot {
    width: 9px; height: 9px; border-radius: 50%;
    background: var(--ink);
  }
  .footer-rule {
    position: absolute;
    left: 0; bottom: 0;
    width: 100%; height: 7px;
    background: var(--navy-deep);
  }
</style>
</head>
<body>
  <section class="envelope envelope--front">
    <svg class="envelope__flap" viewBox="0 0 462 104">
      <path d="M14 104 L14 18 Q14 4 28 4 L434 4 Q448 4 448 18 L448 104 Z" fill="var(--flap-grey)"/>
    </svg>
    <div class="envelope__body">
      <div class="brand">
        <div class="brand__mark"></div>
        <p class="brand__name">RIBEIRO TAVARES</p>
        <p class="brand__tagline">Advogados &amp; Consultores</p>
      </div>
      <div class="front-stripe"></div>
    </div>
  </section>

  <section class="envelope envelope--back">
    <svg class="envelope__flap" viewBox="0 0 462 104">
      <path d="M14 104 L14 18 Q14 4 28 4 L434 4 Q448 4 448 18 L448 104 Z" fill="var(--flap-light)"/>
    </svg>
    <div class="envelope__body">
      <p class="ghost-name">Ribeiro<br>Tavares</p>
      <div class="footer-accent"></div>
      <div class="contacts">
        <span class="contact">
          <svg viewBox="0 0 24 24"><path d="M6.6 10.8a15 15 0 0 0 6.6 6.6l2.2-2.2a1 1 0 0 1 1-.25 11.4 11.4 0 0 0 3.6.57 1 1 0 0 1 1 1V20a1 1 0 0 1-1 1A17 17 0 0 1 3 4a1 1 0 0 1 1-1h3.5a1 1 0 0 1 1 1c0 1.25.2 2.45.57 3.57a1 1 0 0 1-.25 1z" fill="var(--ink)"/></svg>
          00 0000 0000 | 00 00000 0000
        </span>
        <span class="contact">
          <svg viewBox="0 0 24 24"><rect x="3" y="5" width="18" height="14" fill="none" stroke="var(--ink)" stroke-width="2"/><path d="M3 6l9 7 9-7" fill="none" stroke="var(--ink)" stroke-width="2"/></svg>
          seuemail@seuemail.com.br
        </span>
        <span class="contact">
          <span class="contact__dot"></span>
          /ribeirotavares
        </span>
      </div>
      <div class="footer-rule"></div>
    </div>
  </section>
</body>
</html>
```